IT COMPANYcutting edge tec business card

we are IT company that building any apps.
we need business card in japanese and english
You don’t have to include all information in front one you can attach part of that information to back-side
company name : 株式会社かすみ鳥 (MOSSLARK Inc.)
concept : cutting-edge technology
role : 取締役 (director)
name : 河 泰林 (Ha Taerimmu)
post number : 168-0037
address : 東京都世田谷区北霞台5-08-44 (5-08-44, Kitakasumidai, Setagaya Ku, Tokyo To, 168-0037, Japan)
Tel:+81-3-5917-2843
Mobile:+81-80-7263-5518
Email : taerimha@fieldoflark.com
website : www.fieldoflark.com

we dont have logo so please make it as well
we also looking for designer who can make homapage design.

Designs look the same

Low design quality

Contact Information for Business Card

cutting-edge design and modern for IT

Font styles to use
Sans Serif

Colors
34a6d7
33b8a4
6092c4
3377b5
886aae
6b449b
b868aa
a64599

Requirements
Must have
• Simple but designed

```html
<!DOCTYPE html>
<html lang="ja">
<head>
<meta charset="utf-8">
<title>MOSSLARK Inc. Business Card</title>
<link rel="stylesheet" href="https://fonts.googleapis.com/css2?family=Montserrat:wght@400;500;600;700&family=Noto+Sans+JP:wght@400;500;700&display=swap">
<style>
  :root {
    --bg: #e9ebee;
    --ink: #2b2b2b;
    --ink-soft: #444a50;
    --blue: #2a8fe6;
    --white: #ffffff;
    --black-1: #2a2a2c;
    --black-2: #0f0f10;
    --grey-strip: #8d939c;
  }
  * { box-sizing: border-box; margin: 0; padding: 0; }
  html, body {
    width: 1200px; height: 852px; overflow: hidden;
    background: var(--bg);
    font-family: "Montserrat", "Noto Sans JP", sans-serif;
  }
  .sheet {
    width: 1200px; height: 852px;
    display: flex; align-items: center; justify-content: center; gap: 30px;
  }
  .card {
    position: relative;
    width: 560px; height: 320px;
    border-radius: 16px;
    overflow: hidden;
    box-shadow: 0 10px 30px rgba(0,0,0,.18);
  }

  /* Back side */
  .card--back {
    background: radial-gradient(ellipse at 40% 30%, var(--black-1), var(--black-2));
    color: var(--white);
  }
  .card--back .brand {
    position: absolute; left: 0; right: 0; top: 100px; text-align: center;
  }
  .brand__jp {
    font-family: "Noto Sans JP", sans-serif; font-weight: 500;
    color: var(--blue); font-size: 32px; letter-spacing: 1px; line-height: 1.1;
  }
  .brand__en {
    font-family: "Montserrat", sans-serif; font-weight: 400;
    font-size: 38px; letter-spacing: 2px; line-height: 1.15;
  }
  .card--back .site {
    position: absolute; left: 0; right: 0; bottom: 44px; text-align: center;
    font-size: 13px; letter-spacing: 1px; color: var(--white);
  }
  .site__accent { color: var(--blue); }

  /* Front side */
  .card--front { background: var(--white); color: var(--ink); }
  .card--front .brand {
    position: absolute; left: 30px; top: 92px;
  }
  .card--front .brand__jp { font-size: 22px; }
  .card--front .brand__en { font-size: 26px; color: var(--ink-soft); }

  .contact {
    position: absolute; right: 26px; top: 26px;
    list-style: none; text-align: right;
    font-size: 11.5px; line-height: 1.55; color: var(--ink);
  }
  .contact li { display: flex; justify-content: flex-end; align-items: center; gap: 6px; }
  .contact svg { width: 10px; height: 10px; flex: none; }

  .person-jp {
    position: absolute; right: 30px; top: 126px; text-align: right;
    font-family: "Noto Sans JP", sans-serif; font-size: 13px; line-height: 1.45;
  }
  .person-jp__name { color: var(--blue); font-weight: 500; }
  .rule { position: absolute; height: 1.5px; background: var(--blue); }
  .rule--jp { right: 26px; top: 170px; width: 260px; }
  .address-jp {
    position: absolute; right: 30px; top: 178px; text-align: right;
    font-family: "Noto Sans JP", sans-serif; font-size: 13px; line-height: 1.5;
  }

  .person-en {
    position: absolute; left: 30px; top: 196px;
    font-size: 13px; line-height: 1.45;
  }
  .person-en__name { color: var(--blue); font-weight: 700; }
  .person-en__role { color: var(--ink-soft); }
  .rule--en { left: 30px; top: 236px; width: 220px; }
  .address-en {
    position: absolute; left: 30px; top: 244px;
    font-size: 11.5px; line-height: 1.45; color: var(--ink-soft);
  }
  .corner { position: absolute; inset: 0; width: 100%; height: 100%; }
</style>
</head>
<body>
<main class="sheet">

  <section class="card card--back" aria-label="Card back">
    <div class="brand">
      <p class="brand__jp">株式会社かすみ鳥</p>
      <p class="brand__en">MOSSLARK Inc.</p>
    </div>
    <p class="site">www.<span class="site__accent">fieldoflark</span>.com</p>
  </section>

  <section class="card card--front" aria-label="Card front">
    <svg class="corner" viewBox="0 0 560 320" preserveAspectRatio="none" aria-hidden="true">
      <polygon points="0,306 392,306 386,320 0,320" fill="var(--grey-strip)"/>
      <polygon points="408,268 560,252 560,320 392,320" fill="var(--blue)"/>
    </svg>

    <div class="brand">
      <p class="brand__jp">株式会社かすみ鳥</p>
      <p class="brand__en">MOSSLARK Inc.</p>
    </div>

    <ul class="contact">
      <li>+81-3-5917-2843
        <svg viewBox="0 0 10 10"><path d="M2 1l2 2-1 1.2c.6 1.2 1.6 2.2 2.8 2.8L7 6l2 2-1.2 1.3C4.5 9 1 5.5.7 2.2z" fill="var(--blue)"/></svg></li>
      <li>+81-80-7263-5518
        <svg viewBox="0 0 10 10"><rect x="2.5" y="0.5" width="5" height="9" rx="1" fill="none" stroke="var(--blue)"/><circle cx="5" cy="8" r=".6" fill="var(--blue)"/></svg></li>
      <li>taerimha@fieldoflark.com
        <svg viewBox="0 0 10 10"><rect x=".5" y="2" width="9" height="6" fill="none" stroke="var(--blue)"/><path d="M.5 2L5 5.5 9.5 2" fill="none" stroke="var(--blue)"/></svg></li>
      <li><span>www.<span class="site__accent">fieldoflark</span>.com</span>
        <svg viewBox="0 0 10 10"><circle cx="5" cy="5" r="4.5" fill="var(--blue)"/><path d="M.5 5h9M5 .5c-2.5 3-2.5 6 0 9M5 .5c2.5 3 2.5 6 0 9" fill="none" stroke="var(--white)" stroke-width=".7"/></svg></li>
    </ul>

    <div class="person-jp">
      <p class="person-jp__name">河 泰林</p>
      <p>取締役</p>
    </div>
    <div class="rule rule--jp"></div>
    <div class="address-jp">
      <p>168-0037</p>
      <p>東京都世田谷区北霞台5-08-44</p>
    </div>

    <div class="person-en">
      <p class="person-en__name">Ha Taerimmu</p>
      <p class="person-en__role">Director</p>
    </div>
    <div class="rule rule--en"></div>
    <address class="address-en" style="font-style:normal">
      (5-08-44, Kitakasumidai,<br>
      Setagaya Ku, Tokyo To,<br>
      168-0037, Japan)
    </address>
  </section>

</main>
</body>
</html>
```